Coffeeshop menu for filter tip

We want to have a cannabis (coffeeshop) menu in the size 25mm wide x 60mm wide. Some examples attached.

it must have the following text:
Menu

WEED p/g
Vortigan €16
Tangerosa €14
Dusk Rover €14
Mangolina €16
Ultra Fern €14
Amber Hermit €14

HASH p/g
Nepali Bronze €12
Velvet Ember€11
Cedar Pine €14
Red Fable €10

Target Market(s)

tourist in Amsterdam

Requirements
Nice to have
• cannabis sign leaf
• No Cigarettes allowed symbol

```html
<!DOCTYPE html>
<html lang="en">
<head>
<meta charset="utf-8">
<title>Coffeeshop Menu</title>
<link rel="stylesheet" href="https://fonts.googleapis.com/css2?family=Questrial&display=swap">
<style>
  :root {
    --bg-top: #0d0d0d;
    --bg-bottom: #222322;
    --panel: #020202;
    --accent: #fff35c;
    --ink: #ffffff;
    --muted: #9a9a9a;
    --leaf: #2a2c2a;
    --skyline: #0a0a0a;
  }
  * { margin: 0; padding: 0; box-sizing: border-box; }
  html, body { width: 1200px; height: 2880px; overflow: hidden; }
  body {
    position: relative;
    font-family: "Questrial", sans-serif;
    background: linear-gradient(180deg, var(--bg-top) 0%, #161716 45%, var(--bg-bottom) 85%);
    color: var(--ink);
  }
  .leaf-decor {
    position: absolute;
    border-radius: 50%;
    background: radial-gradient(circle, var(--leaf) 0%, rgba(42,44,42,0) 70%);
    opacity: .7;
  }
  .leaf-decor--top { left: 700px; top: -120px; width: 560px; height: 480px; }
  .leaf-decor--left { left: -260px; top: 700px; width: 520px; height: 900px; }
  .leaf-decor--mid { left: 200px; top: 1300px; width: 900px; height: 500px; }
  .leaf-decor--low { left: -200px; top: 1900px; width: 700px; height: 600px; }

  .no-smoking {
    position: absolute; top: 46px; left: 0; width: 1200px;
    display: flex; justify-content: center; align-items: center; gap: 20px;
    font-size: 58px; letter-spacing: 14px; line-height: 1;
  }
  .no-smoking svg { width: 70px; height: 70px; }

  .section-title {
    position: absolute; display: flex; justify-content: space-between;
    color: var(--accent); font-size: 136px; font-weight: 400; line-height: 1;
  }
  .weed-title { left: 124px; top: 160px; width: 720px; }
  .hash-title { left: 396px; top: 1512px; width: 690px; }

  .unit { position: absolute; color: var(--muted); font-size: 64px; line-height: 1; }
  .weed-unit { right: 125px; top: 256px; }
  .hash-unit { left: 136px; top: 1600px; }

  .panel { position: absolute; left: 0; top: 0; }
  .panel svg { position: absolute; left: 0; top: 0; }

  .row {
    position: absolute; display: flex; align-items: center;
    font-size: 94px; line-height: 1; height: 120px;
  }
  .row .name { color: var(--accent); text-transform: uppercase; letter-spacing: 1px; white-space: nowrap; }
  .row .price { color: var(--ink); white-space: nowrap; }
  .weed-row { left: 112px; width: 963px; justify-content: space-between; }
  .hash-row { left: 118px; }
  .hash-row .price { width: 202px; }

  .skyline {
    position: absolute; left: 0; top: 2440px; width: 1200px; height: 220px;
    background: linear-gradient(180deg, rgba(10,10,10,0) 0%, var(--skyline) 70%);
  }
  .menu-band {
    position: absolute; left: 0; top: 2656px; width: 1200px; height: 224px;
    background: var(--panel);
  }
  .menu-title {
    position: absolute; left: 244px; top: 2690px; width: 720px;
    display: flex; justify-content: space-between;
    font-size: 150px; font-weight: 400; line-height: 1; color: var(--ink);
  }
</style>
</head>
<body>
  <div class="leaf-decor leaf-decor--top" role="img" aria-label="Faint cannabis leaf in the background"></div>
  <div class="leaf-decor leaf-decor--left" role="img" aria-label="Faint cannabis leaf in the background"></div>
  <div class="leaf-decor leaf-decor--mid" role="img" aria-label="Faint cannabis leaf in the background"></div>
  <div class="leaf-decor leaf-decor--low" role="img" aria-label="Faint cannabis leaf in the background"></div>

  <header class="no-smoking">
    <span>NO CIGARETTES</span>
    <svg viewBox="0 0 70 70" aria-hidden="true">
      <circle cx="35" cy="35" r="30" fill="none" stroke="#fff" stroke-width="6"/>
      <rect x="14" y="33" width="38" height="8" fill="#fff"/>
      <rect x="54" y="33" width="3" height="8" fill="#fff"/>
      <line x1="14" y1="14" x2="56" y2="56" stroke="#fff" stroke-width="6"/>
    </svg>
  </header>

  <div class="panel weed-panel">
    <svg width="1200" height="1480" viewBox="0 0 1200 1480">
      <polygon points="64,312 944,312 944,184 1136,184 1136,1470 1104,1470 1104,1440 64,1440" fill="var(--panel)"/>
    </svg>
  </div>
  <h2 class="section-title weed-title"><span>W</span><span>E</span><span>E</span><span>D</span></h2>
  <span class="unit weed-unit">p/g</span>

  <div class="row weed-row" style="top:396px"><span class="name">Vortigan</span><span class="price">€16</span></div>
  <div class="row weed-row" style="top:572px"><span class="name">Tangerosa</span><span class="price">€14</span></div>
  <div class="row weed-row" style="top:748px"><span class="name">Dusk Rover</span><span class="price">€14</span></div>
  <div class="row weed-row" style="top:921px"><span class="name">Mangolina</span><span class="price">€16</span></div>
  <div class="row weed-row" style="top:1097px"><span class="name">Ultra Fern</span><span class="price">€14</span></div>
  <div class="row weed-row" style="top:1273px"><span class="name">Amber Hermit</span><span class="price">€14</span></div>

  <div class="panel hash-panel">
    <svg width="1200" height="2460" viewBox="0 0 1200 2460">
      <polygon points="64,1528 224,1528 352,1656 1136,1656 1136,2424 88,2424 88,2450 64,2450" fill="var(--panel)"/>
    </svg>
  </div>
  <h2 class="section-title hash-title"><span>H</span><span>A</span><span>S</span><span>H</span></h2>
  <span class="unit hash-unit">p/g</span>

  <div class="row hash-row" style="top:1735px"><span class="price">€12</span><span class="name">Nepali Bronze</span></div>
  <div class="row hash-row" style="top:1911px"><span class="price">€11</span><span class="name">Velvet Ember</span></div>
  <div class="row hash-row" style="top:2087px"><span class="price">€14</span><span class="name">Cedar Pine</span></div>
  <div class="row hash-row" style="top:2263px"><span class="price">€10</span><span class="name">Red Fable</span></div>

  <div class="skyline" role="img" aria-label="Silhouette of the Amsterdam city skyline"></div>

  <footer class="menu-band"></footer>
  <h1 class="menu-title"><span>M</span><span>E</span><span>N</span><span>U</span></h1>
</body>
</html>
```